Hello my name is Colin, I am Starting a business called Harbor Health and fitness and am in need of a memorable business card.
It is a personal training studio. I have added the logo that i would like to be on the left center om my business card. i would like room left up the top for a heading sentence such as. "Is your body shocking for all the wrong reasons". there must be room left on the right of the logo below the main heading for 3 sub headings.
then under those 3 headings and logo room for another larger heading eg. "give me a call and learn how to eat chocolate, drink bear and have great sex". in what room is left i would like to be used for my contact details, use I'm Colin Pettersby your fitness expert on the left then on the right Phone, Email and website space in at least 12 Point. Very specific i know :) now onto the back, for the back i would like an eye catching graphic and room for one main headline and 3 bullet points centered just write anything i will choose what to put in them when i pick a winner. Thank you very much for sticking through all of that :) i appreciate you taking the time to read it and hopefully undergo designing me a business card.
I can't wait to see the designs!

Target Market(s)

slightly more towards females although it would probably be best if it was targeted towards both sexes

Industry/Entity Type

Training

Requirements
Nice to have
• I would love to see if anyone could come up with a design that would really make my card stand out and be memorable.
Should not have
• tacky fitness photos of abs and muscles etc.

```html
<!DOCTYPE html>
<html lang="en">
<head>
<meta charset="utf-8">
<title>Harbor Health and Fitness – Business Card</title>
<link href="https://fonts.googleapis.com/css2?family=Open+Sans:wght@400;600;700;800&display=swap" rel="stylesheet">
<style>
  :root{
    --navy:#1d4a85;
    --navy-deep:#0f2d5c;
    --navy-light:#2d62a6;
    --paper:#ffffff;
    --ink:#2b3a55;
    --ghost:#d9dbe0;
    --backdrop:#e9ebef;
  }
  *{box-sizing:border-box;margin:0;padding:0}
  html,body{width:1200px;height:1024px;overflow:hidden;background:var(--backdrop);font-family:"Open Sans",Arial,sans-serif}
  .canvas{position:relative;width:1200px;height:1024px}
  .card{position:absolute;left:180px;width:840px;height:480px;overflow:hidden;box-shadow:0 6px 18px rgba(0,0,0,.18)}
  .card-front{top:24px;background:var(--paper)}
  .card-back{top:528px;background:radial-gradient(circle at 55% 60%,var(--navy-light),var(--navy-deep) 80%)}
  .band{position:absolute;inset:0;width:100%;height:100%}
  .headline{position:absolute;left:22px;top:44px;width:560px;color:var(--paper);white-space:nowrap}
  .headline-main{font-weight:800;font-size:16.5px;letter-spacing:.2px;text-transform:uppercase;line-height:1.3}
  .headline-sub{font-weight:600;font-size:10.5px;text-transform:uppercase;margin-top:4px;line-height:1.3}
  .figure-art{position:absolute;right:60px;top:20px;width:300px;height:230px;border-radius:40%;background:radial-gradient(ellipse at center,var(--ghost),rgba(255,255,255,0) 70%)}
  .figure-art-back{position:absolute;left:60px;top:30px;width:420px;height:260px;border-radius:45%;background:radial-gradient(ellipse at center,rgba(90,140,210,.45),rgba(90,140,210,0) 70%)}
  .brand{position:absolute;display:flex;align-items:center;gap:12px}
  .brand-dot{width:22px;height:22px;border-radius:50%;background:var(--navy)}
  .brand-name{font-weight:700;color:var(--navy);line-height:1}
  .brand-tag{font-weight:400;color:var(--ink)}
  .front-brand{left:70px;top:170px}
  .front-brand .brand-name{font-size:72px}
  .front-tag{position:absolute;left:104px;top:254px;font-size:20px}
  .contact{position:absolute;left:70px;top:300px;list-style:none;font-size:21px;color:var(--ink)}
  .contact li{display:flex;align-items:center;gap:10px;line-height:1.45}
  .contact svg{width:16px;height:16px;fill:var(--navy)}
  .person{position:absolute;right:50px;top:250px;text-align:left}
  .person-name{font-weight:800;font-size:24px;color:var(--navy)}
  .person-role{font-size:17px;color:var(--ink)}
  .back-brand{left:420px;top:220px;flex-direction:column;align-items:flex-start;gap:4px}
  .back-brand .brand-row{display:flex;align-items:center;gap:12px}
  .back-brand .brand-dot{background:var(--paper)}
  .back-brand .brand-name{font-size:84px;color:var(--paper)}
  .back-brand .brand-tag{color:var(--paper);font-size:22px;padding-left:34px}
  .back-brand .brand-web{color:#cfe0f5;font-size:16px;padding-left:34px}
</style>
</head>
<body>
<main class="canvas">
  <section class="card card-front" aria-label="Business card front">
    <svg class="band" viewBox="0 0 840 480" preserveAspectRatio="none" aria-hidden="true">
      <polygon points="0,34 590,34 570,108 0,108" fill="var(--navy)"/>
      <polygon points="590,34 608,34 588,108 570,108" fill="var(--navy-light)"/>
      <polygon points="300,440 840,440 840,480 280,480" fill="var(--navy)"/>
      <rect x="300" y="432" width="540" height="3" fill="var(--navy-light)"/>
    </svg>
    <div class="headline">
      <p class="headline-main">Is your body shocking for all the wrong reasons</p>
      <p class="headline-sub">Give me a call and learn how to eat chocolate, drink bear and have great sex</p>
    </div>
    <div class="figure-art" role="img" aria-label="Faint grey silhouette of a person running"></div>
    <div class="brand front-brand">
      <span class="brand-dot"></span>
      <span class="brand-name">Harbor</span>
    </div>
    <p class="brand-tag front-tag">Health and Fitness</p>
    <ul class="contact">
      <li><svg viewBox="0 0 16 16"><path d="M3 1l3 3-1.5 2a9 9 0 0 0 5.5 5.5L12 10l3 3-2 2C6 15 1 10 1 3z"/></svg>000-000-000</li>
      <li><svg viewBox="0 0 16 16"><path d="M1 3h14v10H1zM1 3l7 6 7-6" stroke="#fff" stroke-width="1"/></svg>name@harborfitstudio.com</li>
      <li><svg viewBox="0 0 16 16"><circle cx="8" cy="8" r="7"/><path d="M1 8h14M8 1c-3 3-3 11 0 14M8 1c3 3 3 11 0 14" stroke="#fff" fill="none"/></svg>www.harborfitstudio.com</li>
    </ul>
    <div class="person">
      <p class="person-name">Colin Pettersby</p>
      <p class="person-role">fitness expert</p>
    </div>
  </section>

  <section class="card card-back" aria-label="Business card back">
    <div class="figure-art-back" role="img" aria-label="Faint blue silhouette of a person running"></div>
    <div class="brand back-brand">
      <div class="brand-row">
        <span class="brand-dot"></span>
        <span class="brand-name">Harbor</span>
      </div>
      <span class="brand-tag">Health and Fitness</span>
      <span class="brand-web">www.harborfitstudio.com</span>
    </div>
  </section>
</main>
</body>
</html>
```